stationary deign for trucking company

im a trucking company looking for a professional set of stationary designs i deliver goods from point a to b
Updates

When submitting stationary designs I need envelope design, letterhead, cards, I’d badge etc

Industry/Entity Type

Trucking Company

Requirements
Must have
• must have letter head, business card, envelope, fax sheet, id badge, folder, thank you card, notebook, invoice sheet.
Nice to have
• nice to have them all custom made (letterhead,envelope, business card, I’d badge etc
Should not have
• must not have prepaid sign want i unique design for items

```html
<!DOCTYPE html>
<html lang="en">
<head>
<meta charset="utf-8">
<title>Hartwell Freight + Logistics — Stationery Set</title>
<link rel="stylesheet" href="https://fonts.googleapis.com/css2?family=Montserrat:wght@500;600&family=Arimo:wght@400;700&display=swap">
<style>
  :root{
    --bg:#dcd9d6;
    --paper:#ffffff;
    --folder:#c9cacc;
    --card-grey:#d3d4d6;
    --ink:#1c1c1e;
    --muted:#8a8a8e;
    --blue:#1f5fb0;
    --blue-soft:#2e69b8;
    --rule:#2a2a2c;
  }
  *{box-sizing:border-box;margin:0;padding:0}
  html,body{width:1200px;height:904px;overflow:hidden}
  body{background:var(--bg);position:relative;font-family:"Arimo",Arial,sans-serif;color:var(--ink)}
  .piece{position:absolute;box-shadow:0 6px 14px rgba(0,0,0,.18)}

  .brand{display:flex;align-items:center;gap:7px}
  .brand-mark{width:10px;height:10px;background:var(--blue);flex:none}
  .brand-text{display:flex;flex-direction:column;align-items:center;font-family:"Montserrat",sans-serif;font-weight:600;color:var(--ink);line-height:1}
  .brand-name{letter-spacing:.14em}
  .brand-sub{letter-spacing:.22em;margin-top:3px}

  /* Letterhead */
  .letterhead{left:100px;top:28px;width:345px;height:492px;background:var(--paper)}
  .lh-header{position:absolute;top:30px;left:0;right:0;height:16px}
  .lh-header .bar-blue{position:absolute;left:0;top:6px;width:32px;height:4px;background:var(--blue)}
  .lh-header .bar-dark{position:absolute;left:182px;right:0;top:6px;height:4px;background:var(--rule)}
  .lh-header .brand{position:absolute;left:40px;top:-2px}
  .lh-header .brand-name{font-size:14px}
  .lh-header .brand-sub{font-size:4.5px}
  .lh-body{position:absolute;left:39px;right:38px;top:116px;font-size:6.4px;line-height:10.6px;color:#6d6d71}
  .lh-body p{margin-bottom:10px}
  .lh-body p+p+p{margin-top:14px}
  .lh-footer{position:absolute;left:8px;right:0;bottom:12px;font-size:5.2px;color:#444;display:flex;gap:8px;align-items:center}
  .lh-footer .ico{display:inline-block;width:5px;height:5px;border-radius:50%;background:var(--blue);margin-right:2px;vertical-align:middle}
  .lh-foot-bar{position:absolute;left:0;right:0;bottom:0;height:5px;background:var(--rule)}
  .lh-foot-bar::before{content:"";position:absolute;left:0;top:-2px;width:60%;height:2px;background:var(--blue)}
  .lh-web{position:absolute;right:4px;bottom:6px;background:var(--rule);color:#fff;font-size:4.5px;padding:2px 4px}

  /* Folder */
  .folder{left:436px;top:70px;width:345px;height:492px;background:var(--folder)}
  .folder .brand{position:absolute;left:0;right:0;top:242px;justify-content:center}
  .folder .brand-mark{width:14px;height:14px}
  .folder .brand-name{font-size:32px;letter-spacing:.12em}
  .folder .brand-sub{font-size:9.5px;margin-top:9px;letter-spacing:.24em}
  .folder-web{position:absolute;left:0;right:0;bottom:12px;text-align:center;font-size:7.6px;font-weight:700;color:#3d3d40}
  .folder-base{position:absolute;left:0;right:0;bottom:0;height:3px;background:var(--rule)}
  .folder-base::after{content:"";position:absolute;left:40%;width:22%;height:3px;background:var(--blue)}

  /* Business cards */
  .card-front{left:828px;top:82px;width:155px;height:88px;background:var(--card-grey)}
  .card-front .brand{position:absolute;left:0;right:0;top:36px;justify-content:center}
  .card-front .brand-name{font-size:11px}
  .card-front .brand-sub{font-size:3.6px}
  .card-back{left:830px;top:208px;width:155px;height:88px;background:var(--paper)}
  .card-back .brand{position:absolute;left:8px;top:36px;gap:4px}
  .card-back .brand-mark{width:6px;height:6px}
  .card-back .brand-name{font-size:8px}
  .card-back .brand-sub{font-size:2.8px}
  .card-back .divider{position:absolute;left:74px;top:14px;width:1px;height:56px;background:#9a9aa0}
  .card-back .details{position:absolute;left:80px;top:16px;font-size:4.2px;line-height:6.4px;color:#333}
  .card-back .details b{font-size:5px;color:var(--ink)}
  .card-back .base{position:absolute;left:0;right:0;bottom:0;height:3px;background:var(--blue)}

  /* Notebook */
  .notebook{left:828px;top:328px;width:148px;height:230px;background:var(--card-grey);border-radius:0 10px 10px 0}
  .notebook .spine{position:absolute;left:0;top:0;bottom:0;width:6px;background:#b9babc}
  .notebook .band{position:absolute;left:104px;top:0;bottom:0;width:7px;background:#4a4a4c}
  .notebook .brand{position:absolute;left:0;right:0;top:112px;justify-content:center}
  .notebook .brand-name{font-size:12px}
  .notebook .brand-sub{font-size:3.8px}
  .notebook .web{position:absolute;left:48px;bottom:6px;font-size:3.4px;color:#555}

  /* Thank you card */
  .thanks{left:70px;top:590px;width:340px;height:232px;background:#ececea;overflow:hidden}
  .thanks .wave{position:absolute;inset:0}
  .thanks .brand{position:absolute;left:22px;top:26px}
  .thanks .brand-name{font-size:15px}
  .thanks .brand-sub{font-size:5px}
  .thanks .script{position:absolute;left:90px;top:100px;width:200px;height:62px;background:linear-gradient(90deg,#dfe4ee,#c9d4e8);border-radius:4px}
  .thanks .foot{position:absolute;left:0;right:0;bottom:0;height:16px;background:var(--rule);color:#fff;font-size:5.2px;display:flex;align-items:center;gap:12px;padding-left:12px}

  /* ID badge */
  .badge{left:435px;top:665px;width:300px;height:150px;background:var(--paper);border-radius:6px;border:3px solid #eceded}
  .badge .photo{position:absolute;left:14px;top:10px;width:92px;height:82px;background:linear-gradient(180deg,#e9e9ea,#b9bcc2 60%,#3a3d45)}
  .badge .brand{position:absolute;left:126px;top:42px}
  .badge .brand-name{font-size:16px}
  .badge .brand-sub{font-size:5.2px}
  .badge .strip{position:absolute;left:6px;right:6px;bottom:8px;height:38px;background:var(--blue-soft);color:#fff;padding:6px 14px;display:flex;justify-content:space-between;border-radius:0 0 4px 4px}
  .badge .strip .name{font-size:10px;font-weight:700}
  .badge .strip .role{font-size:7px;margin-top:2px}
  .badge .strip .num{text-align:right;font-size:8.5px;line-height:11px}

  /* Envelope */
  .envelope{left:758px;top:676px;width:358px;height:178px;background:var(--paper)}
  .envelope .flap{position:absolute;left:38px;top:-82px;width:358px;height:82px;background:#c6c7c9;border-radius:10px 10px 0 0;z-index:-1}
  .envelope .brand{position:absolute;left:12px;top:22px;gap:5px}
  .envelope .brand-mark{width:8px;height:8px}
  .envelope .brand-name{font-size:10.5px}
  .envelope .brand-sub{font-size:3.4px}
  .envelope .addr{position:absolute;left:12px;top:38px;font-size:4.2px;font-weight:700;color:var(--blue)}
  .envelope .base{position:absolute;left:0;right:0;bottom:0;height:3px;background:var(--rule)}
  .envelope .base::after{content:"";position:absolute;left:38%;width:34%;height:3px;background:var(--blue)}
</style>
</head>
<body>

<section class="piece letterhead" aria-label="Letterhead">
  <div class="lh-header">
    <span class="bar-blue"></span>
    <div class="brand">
      <span class="brand-mark"></span>
      <div class="brand-text"><span class="brand-name">HARTWELL</span><span class="brand-sub">FREIGHT + LOGISTICS</span></div>
    </div>
    <span class="bar-dark"></span>
  </div>
  <div class="lh-body">
    <p>Lorem Ipsum is simply dummy text of the printing and typesetting industry. Lorem Ipsum has been the industry's standard dummy text ever since the 1500s, when an unknown printer took a galley of type and scrambled it to make a type specimen book. It has survived not only five centuries, but also the leap into electronic typesetting, remaining essentially unchanged. It was popularised in the 1960s with the release of Letraset sheets containing Lorem Ipsum passages, and more recently with desktop publishing software including versions of Lorem Ipsum.</p>
    <p>It is a long established fact that a reader will be distracted by the readable content of a page when looking at its layout. The point of using Lorem Ipsum is that it has a more-or-less normal distribution of letters, as opposed to using 'Content here, content here', making it look like readable English. Many desktop publishing packages and web page editors now use Lorem Ipsum as their default model text, and a search for 'lorem ipsum' will uncover many web sites still in their infancy.</p>
    <p>Contrary to popular belief, Lorem Ipsum is not simply random text. It has roots in a piece of classical Latin literature from 45 BC, making it over 2000 years old. A Latin professor looked up one of the more obscure Latin words, consectetur, from a Lorem Ipsum passage, and going through the cites of the word in classical literature, discovered the undoubtable source. The generated Lorem Ipsum is therefore always free from repetition, injected humour, or non-characteristic words etc.</p>
  </div>
  <div class="lh-footer">
    <span><span class="ico"></span>001 Example Dr, Example City, CA 00000</span>
    <span><span class="ico"></span>000-000-0005</span>
    <span><span class="ico"></span>info@hartwellfreight.com</span>
  </div>
  <span class="lh-web">www.hartwellfreight.com</span>
  <div class="lh-foot-bar"></div>
</section>

<section class="piece folder" aria-label="Presentation folder">
  <div class="brand">
    <span class="brand-mark"></span>
    <div class="brand-text"><span class="brand-name">HARTWELL</span><span class="brand-sub">FREIGHT + LOGISTICS</span></div>
  </div>
  <div class="folder-web">www.hartwellfreight.com</div>
  <div class="folder-base"></div>
</section>

<section class="piece card-front" aria-label="Business card front">
  <div class="brand">
    <span class="brand-mark"></span>
    <div class="brand-text"><span class="brand-name">HARTWELL</span><span class="brand-sub">FREIGHT + LOGISTICS</span></div>
  </div>
</section>

<section class="piece card-back" aria-label="Business card back">
  <div class="brand">
    <span class="brand-mark"></span>
    <div class="brand-text"><span class="brand-name">HARTWELL</span><span class="brand-sub">FREIGHT + LOGISTICS</span></div>
  </div>
  <span class="divider"></span>
  <div class="details">
    <b>Example Name</b><br>
    Operations Manager<br>
    Level 00, 00 Main Street, Example<br>
    0000 000 000 · 0000 000 000<br>
    info@hartwellfreight.com<br>
    www.hartwellfreight.com
  </div>
  <div class="base"></div>
</section>

<section class="piece notebook" aria-label="Notebook cover">
  <span class="spine"></span>
  <div class="brand">
    <div class="brand-text"><span class="brand-name">HARTWELL</span><span class="brand-sub">FREIGHT + LOGISTICS</span></div>
  </div>
  <span class="band"></span>
  <span class="web">www.hartwellfreight.com</span>
</section>

<section class="piece thanks" aria-label="Thank you card">
  <svg class="wave" viewBox="0 0 340 232" aria-hidden="true">
    <path d="M0 0H340V40C250 40 200 60 150 120C110 170 60 200 0 200Z" fill="#c3c4c7"/>
    <path d="M0 200C60 200 110 170 150 120C200 60 250 40 340 40" fill="none" stroke="#ffffff" stroke-width="3"/>
    <line x1="40" y1="190" x2="300" y2="130" stroke="var(--blue)" stroke-width="1"/>
  </svg>
  <div class="brand">
    <span class="brand-mark"></span>
    <div class="brand-text"><span class="brand-name">HARTWELL</span><span class="brand-sub">FREIGHT + LOGISTICS</span></div>
  </div>
  <div class="script" role="img" aria-label="Hand lettered 'Thank you' in blue script"></div>
  <div class="foot">
    <span>001 Example Dr, Example City, CA 00000</span>
    <span>000-000-0005</span>
    <span>contact@hartwellfreight.com</span>
  </div>
</section>

<section class="piece badge" aria-label="Employee ID badge">
  <div class="photo" role="img" aria-label="Employee portrait photo"></div>
  <div class="brand">
    <div class="brand-text"><span class="brand-name">HARTWELL</span><span class="brand-sub">FREIGHT + LOGISTICS</span></div>
  </div>
  <div class="strip">
    <div><div class="name">Employee Name</div><div class="role">Employee Designation</div></div>
    <div class="num">Card Number<br>0000000000000000</div>
  </div>
</section>

<section class="piece envelope" aria-label="Envelope">
  <div class="flap" role="img" aria-label="Grey envelope flap with a light geometric pattern"></div>
  <div class="brand">
    <span class="brand-mark"></span>
    <div class="brand-text"><span class="brand-name">HARTWELL</span><span class="brand-sub">FREIGHT + LOGISTICS</span></div>
  </div>
  <div class="addr">Level 00, 00 Example Street, Example, 2000</div>
  <div class="base"></div>
</section>

</body>
</html>
```